Health & Beauty Company- Business Card Design

Two-sided business card design and logo design.

Company markets and sells otc treatments for the health and beauty industry. Marketing products to doctors, pharmacists and retail drug companies like dorvellas, pmn and velo mart.

Designs should be submitted as vector based PDFs. To keep your text in vector format, our printer recommends applications like Adobe Illustrator, Adobe InDesign and more recent versions of Adobe Photoshop.

Target Market(s)

Drug stores, doctors and pharmacists

Industry/Entity Type

Printer

Requirements
Must have
• Back side of business card should include company logo and our tagline: "Elevating Everyday Wellness & Skin Care"

Company name acronym must be included: NRTK

```html
<!DOCTYPE html>
<html lang="en">
<head>
<meta charset="utf-8">
<title>NRTK Business Card</title>
<link href="https://fonts.googleapis.com/css2?family=Open+Sans:wght@400;600;700&display=swap" rel="stylesheet">
<style>
  :root {
    --bg: #e6e6ef;
    --card-light: #f4f4f4;
    --card-dark: #1c1c1c;
    --ink-dark: #1e1e1e;
    --ink-light: #f2f2f2;
    --ink-muted: #a9a9a9;
    --rule: #5a5a5a;
  }
  * { margin: 0; padding: 0; box-sizing: border-box; }
  html, body { width: 1200px; height: 900px; overflow: hidden; }
  body {
    background: var(--bg);
    font-family: "Open Sans", Arial, sans-serif;
    position: relative;
  }
  .card {
    position: absolute;
    width: 525px;
    height: 300px;
    border-radius: 3px;
    box-shadow: 0 10px 30px rgba(0,0,0,0.18);
  }
  .card--front {
    left: 70px; top: 130px;
    background: var(--card-light);
    display: flex; align-items: center; justify-content: center;
  }
  .brand { display: flex; align-items: center; gap: 18px; }
  .brand__mark {
    width: 84px; height: 84px; border-radius: 50%;
    background: var(--ink-dark);
    flex: none;
  }
  .brand__name {
    font-size: 50px; font-weight: 700; color: var(--ink-dark);
    line-height: 1; letter-spacing: 1px;
  }
  .brand__tagline {
    font-size: 13px; font-weight: 600; color: var(--ink-dark);
    margin-top: 6px; white-space: nowrap;
  }
  .card--back {
    left: 605px; top: 470px;
    background: var(--card-dark);
    color: var(--ink-light);
    display: flex; align-items: center;
    padding: 0 36px;
  }
  .person { width: 250px; text-align: right; padding-right: 22px; }
  .person__name { font-size: 20px; font-weight: 700; white-space: nowrap; }
  .person__title { font-size: 11px; color: var(--ink-muted); margin-top: 2px; }
  .person__address { font-size: 10px; color: var(--ink-muted); margin-top: 8px; white-space: nowrap; }
  .divider { width: 1px; height: 110px; background: var(--rule); flex: none; }
  .contacts { list-style: none; padding-left: 20px; }
  .contacts li {
    display: flex; align-items: center; gap: 10px;
    font-size: 12.5px; line-height: 1; margin: 7px 0;
    white-space: nowrap;
  }
  .contacts svg { width: 14px; height: 14px; fill: var(--ink-light); flex: none; }
</style>
</head>
<body>
  <section class="card card--front">
    <div class="brand">
      <div class="brand__mark"></div>
      <div>
        <div class="brand__name">NRTK</div>
        <div class="brand__tagline">Elevating Everyday Wellness &amp; Skin Care</div>
      </div>
    </div>
  </section>

  <section class="card card--back">
    <div class="person">
      <div class="person__name">Marissa Caldwell</div>
      <div class="person__title">President &amp; CEO</div>
      <div class="person__address">48 Larkspur Lane, Fairview, OR 97024</div>
    </div>
    <div class="divider"></div>
    <ul class="contacts">
      <li>
        <svg viewBox="0 0 16 16" aria-hidden="true"><path d="M3 1h3l1.5 4-2 1.2a9 9 0 0 0 4.3 4.3L11 8.5l4 1.5v3a2 2 0 0 1-2 2A12 12 0 0 1 1 3a2 2 0 0 1 2-2z"/></svg>
        1 000 000 0000
      </li>
      <li>
        <svg viewBox="0 0 16 16" aria-hidden="true"><path d="M4 0h8a1 1 0 0 1 1 1v14a1 1 0 0 1-1 1H4a1 1 0 0 1-1-1V1a1 1 0 0 1 1-1zm1 2v10h6V2zm3 11a1 1 0 1 0 0 2 1 1 0 0 0 0-2z"/></svg>
        1 000 000 0000
      </li>
      <li>
        <svg viewBox="0 0 16 16" aria-hidden="true"><path d="M1 3h14v10H1zm1.5 1.2L8 8.5l5.5-4.3z"/></svg>
        hello@nrtkhealth.com
      </li>
      <li>
        <svg viewBox="0 0 16 16" aria-hidden="true"><circle cx="8" cy="8" r="7"/></svg>
        marissa.nrtk
      </li>
    </ul>
  </section>
</body>
</html>
```